Keto Food Brand Needs Packaging Design and Logo

We need a logo and packaging design for a stand-up food bag for our keto shake mix. We are a health and wellness brand launching our first shake mix product. I would like bold, bright colors. This document goes more in depth . This brand might encompass more than only food so I want the logo to be versatile for supplements and other health products. https://files.plimmerdocs.net/sheet/7qXbRt2LmPzK9vWc4HnJ8sFdYa3GeU6oBiN1kT5rQ0Vx/view?mode=shared See images of logos attached. It doesn't have to be food for the logo but I like the creativity of the ones listed.

Target Market(s)

Keto. Health and Fitness

Logo Text

Zunavo

Font styles to use
Serif
Sans Serif

Colors

Designer to choose colors to be used in the design.

```html
<!DOCTYPE html>
<html lang="en">
<head>
<meta charset="utf-8">
<title>Zunavo Keto Shake – Cheesecake Mix</title>
<link href="https://fonts.googleapis.com/css2?family=Fredoka:wght@600;700&family=Oswald:wght@700&family=Patrick+Hand&display=swap" rel="stylesheet">
<style>
  :root {
    --backdrop: #e4e4e4;
    --orange-deep: #d9561a;
    --orange: #f07a22;
    --amber: #f6a81c;
    --amber-deep: #e08a14;
    --red: #e8242a;
    --yellow: #f7e21a;
    --white: #ffffff;
    --ink: #2a1a10;
    --label-orange: #ec6a24;
  }
  * { margin: 0; padding: 0; box-sizing: border-box; }
  html, body { width: 1200px; height: 740px; overflow: hidden; background: var(--backdrop); }
  .canvas { position: relative; width: 1200px; height: 740px; }
  .label {
    position: absolute; left: 308px; top: 20px; width: 584px; height: 700px; overflow: hidden;
    background: linear-gradient(160deg, var(--orange-deep) 0%, var(--orange) 30%, var(--orange) 45%, var(--amber) 62%, var(--amber) 85%, var(--amber-deep) 100%);
  }
  .corner-flash {
    position: absolute; right: -120px; top: -120px; width: 260px; height: 260px;
    border-radius: 50%; background: var(--red);
  }
  .keto-seal {
    position: absolute; right: 14px; top: 14px; width: 88px; height: 88px;
    border-radius: 50%; border: 3px solid var(--white);
  }
  .brand {
    position: absolute; top: 100px; left: 0; width: 100%; text-align: center;
    font-family: "Fredoka", sans-serif; font-weight: 700; font-size: 36px;
    color: var(--red); letter-spacing: 1px;
  }
  .product-name {
    position: absolute; top: 165px; left: 0; width: 100%; text-align: center;
    font-family: "Fredoka", sans-serif; font-weight: 700; font-size: 62px; line-height: 1;
    color: var(--white);
  }
  .product-name .keto { color: var(--yellow); }
  .band { position: absolute; left: 0; top: 262px; width: 584px; height: 150px; }
  .flavour {
    position: absolute; top: 300px; left: 0; width: 100%; text-align: center;
    font-family: "Oswald", sans-serif; font-weight: 700; font-size: 58px; line-height: 1;
    color: var(--label-orange); word-spacing: 28px; letter-spacing: 1px;
  }
  .hero-art {
    position: absolute; left: 130px; top: 420px; width: 300px; height: 150px;
    border-radius: 50% 50% 46% 46%;
    background: radial-gradient(ellipse at 50% 45%, #fbf6ec 0%, #f1e6d2 45%, rgba(246,168,28,0) 72%);
  }
  .claim {
    position: absolute; font-family: "Patrick Hand", sans-serif; font-size: 13px; line-height: 1;
    color: var(--white); text-align: center; text-transform: uppercase; letter-spacing: 0.5px;
  }
  .claim-keto { left: 128px; top: 440px; transform: rotate(-38deg); }
  .claim-carb { left: 418px; top: 432px; transform: rotate(38deg); }
  .claim-sugar { left: 82px; top: 520px; transform: rotate(-65deg); }
  .claim-taste { left: 448px; top: 520px; transform: rotate(68deg); }
  .arrows { position: absolute; left: 0; top: 0; width: 584px; height: 700px; pointer-events: none; }
  .usage {
    position: absolute; top: 578px; width: 88px; height: 88px; border-radius: 50%;
    background: var(--white); border: 2px solid var(--amber);
    display: flex; flex-direction: column; align-items: center; justify-content: center;
    box-shadow: inset 0 0 0 4px var(--white), inset 0 0 0 5px var(--label-orange);
  }
  .usage svg { width: 22px; height: 22px; margin-bottom: 1px; }
  .usage span {
    font-family: "Fredoka", sans-serif; font-weight: 600; font-size: 19px; color: var(--label-orange);
    line-height: 1;
  }
  .usage-shake { left: 147px; }
  .usage-bake { left: 250px; }
  .usage-freeze { left: 360px; }
  .net-weight {
    position: absolute; top: 676px; left: 0; width: 100%; text-align: center;
    font-family: "Fredoka", sans-serif; font-weight: 600; font-size: 9px; color: var(--ink); letter-spacing: 0.3px;
  }
</style>
</head>
<body>
<main class="canvas">
  <section class="label">
    <div class="corner-flash"></div>
    <div class="keto-seal" aria-hidden="true"></div>

    <div class="brand">Zunavo</div>
    <h1 class="product-name"><span class="keto">KETO</span> SHAKE</h1>

    <svg class="band" viewBox="0 0 584 150" preserveAspectRatio="none" aria-hidden="true">
      <path fill="#ffffff" d="M0 14 L18 10 L30 16 L52 8 L70 14 L96 6 L118 13 L140 9 L162 15 L190 7 L214 12 L236 5 L258 14 L284 9 L306 16 L330 6 L352 12 L378 8 L400 15 L424 7 L448 13 L470 9 L494 15 L518 6 L540 12 L562 8 L584 13
               L584 126 L566 132 L546 125 L526 134 L502 128 L480 136 L456 127 L432 133 L410 126 L386 135 L362 128 L338 134 L316 126 L292 133 L268 127 L246 136 L222 128 L198 134 L174 126 L150 133 L128 127 L104 135 L82 128 L58 134 L36 126 L16 132 L0 127 Z"/>
    </svg>
    <h2 class="flavour">CHEESECAKE MIX</h2>

    <div class="hero-art" role="img" aria-label="Slice of layered cheesecake with caramel drizzle on a splash of cream"></div>

    <span class="claim claim-keto">Keto<br>Friendly</span>
    <span class="claim claim-carb">Low<br>Carb</span>
    <span class="claim claim-sugar">No Added<br>Sugar</span>
    <span class="claim claim-taste">Incredible<br>Taste</span>

    <svg class="arrows" viewBox="0 0 584 700" fill="none" stroke="#ffffff" stroke-width="1.5" stroke-linecap="round" aria-hidden="true">
      <path d="M178 452 Q196 452 204 466"/><path d="M198 462 L204 466 L205 459"/>
      <path d="M404 448 Q390 440 378 448"/><path d="M383 443 L378 448 L384 451"/>
      <path d="M108 558 Q112 578 132 578"/><path d="M126 574 L132 578 L127 583"/>
      <path d="M472 568 Q464 584 446 582"/><path d="M451 578 L446 582 L451 587"/>
    </svg>

    <div class="usage usage-shake">
      <svg viewBox="0 0 24 24" fill="none" stroke="#ec6a24" stroke-width="2" stroke-linecap="round" aria-hidden="true">
        <path d="M9 3h6v3H9z" fill="#ec6a24"/><path d="M8 7h8l-1 14H9z" fill="#ec6a24"/><path d="M4 9v6M20 9v6"/>
      </svg>
      <span>SHAKE</span>
    </div>
    <div class="usage usage-bake">
      <svg viewBox="0 0 24 24" fill="none" stroke="#ec6a24" stroke-width="2" stroke-linecap="round" aria-hidden="true">
        <path d="M3 14h18l-2 6H5z" fill="#ec6a24"/><path d="M5 14c1-4 13-4 14 0"/><path d="M9 4v4M12 3v5M15 4v4"/>
      </svg>
      <span>BAKE</span>
    </div>
    <div class="usage usage-freeze">
      <svg viewBox="0 0 24 24" fill="none" stroke="#ec6a24" stroke-width="2.4" stroke-linecap="round" aria-hidden="true">
        <path d="M12 3v18M3 12h18M5.6 5.6l12.8 12.8M18.4 5.6L5.6 18.4"/>
      </svg>
      <span>FREEZ</span>
    </div>

    <p class="net-weight">DIETARY SUPPLEMENT | NET. WT. 2.0 LB</p>
  </section>
</main>
</body>
</html>
```